Varrow Business Card Design - Professional Flexible and forward thinking. Clean and Easy to follow

Management Consulting Company. I focus on business development and concept and operational review. I need a progressive, simple and professional layout design for the business cards, letterhead and envelops
Professional Flexible and forward thinking. Clean and Easy to follow
Mature Business persons and professionals and Corporations

Target Market(s)

Mature Business persons and professionals and Corporations - Government org.

Industry/Entity Type

Consulting

Contact Information for Business Card

Requirements
Must have
• Marcus Varrow
• President
• Phone - 347.682.1530
• email - Mvarrow@varrowpartners-example.com
• Skype - Marc.varrow
• 2187 Tollbrook Lane
• Suite C
• Larkfield, N.Y. 11492
• USA
Nice to have
• www.varrowpartners-example.com
Should not have
• N/A

```html
<!DOCTYPE html>
<html lang="en">
<head>
<meta charset="utf-8">
<title>Varrow Business Card Design</title>
<link rel="stylesheet" href="https://fonts.googleapis.com/css2?family=Montserrat:wght@400;600&family=EB+Garamond:wght@400;500;600&display=swap">
<style>
  :root {
    --stage: #262626;
    --card-dark: #2c2c2e;
    --card-dark-edge: #232325;
    --paper: #f7f7f7;
    --navy: #0e3f6f;
    --navy-deep: #0a3561;
    --ink-light: #e9edf2;
    --silver: #d9d9d9;
  }
  * { margin: 0; padding: 0; box-sizing: border-box; }
  html, body { width: 1200px; height: 873px; overflow: hidden; }
  body {
    background: var(--stage);
    position: relative;
    font-family: "EB Garamond", Georgia, serif;
  }
  .card {
    position: absolute;
    top: 286px;
    width: 520px;
    height: 300px;
    border-radius: 18px;
    overflow: hidden;
  }

  /* Back of card */
  .card--back {
    left: 50px;
    background: linear-gradient(135deg, var(--card-dark) 0%, var(--card-dark-edge) 100%);
    display: flex;
    flex-direction: column;
    align-items: center;
    justify-content: center;
    gap: 34px;
  }
  .brand {
    display: flex;
    align-items: center;
    gap: 12px;
    font-family: "Montserrat", Arial, sans-serif;
    font-weight: 600;
    letter-spacing: 0.02em;
    text-transform: uppercase;
    white-space: nowrap;
  }
  .brand__square { width: 14px; height: 14px; }
  .card--back .brand { color: var(--silver); font-size: 26px; }
  .card--back .brand__square { background: var(--silver); }
  .website {
    font-family: "Montserrat", Arial, sans-serif;
    font-weight: 600;
    font-size: 11px;
    letter-spacing: 0.18em;
    color: var(--silver);
    white-space: nowrap;
  }

  /* Front of card */
  .card--front {
    left: 630px;
    background: var(--paper);
  }
  .card--front .brand {
    position: absolute;
    top: 70px;
    left: 0;
    right: 0;
    justify-content: center;
    color: var(--navy);
    font-size: 22px;
  }
  .card--front .brand__square { background: var(--navy); }
  .rules {
    position: absolute;
    left: 0; right: 0; top: 150px;
  }
  .rules span {
    display: block;
    height: 2px;
    background: var(--navy);
    margin-bottom: 3px;
  }
  .band {
    position: absolute;
    left: 0; right: 0; top: 166px; bottom: 0;
    background: linear-gradient(180deg, var(--navy) 0%, var(--navy-deep) 100%);
    color: var(--ink-light);
    display: flex;
    align-items: center;
  }
  .contacts {
    width: 280px;
    padding-right: 16px;
    font-size: 13.5px;
    line-height: 27px;
    white-space: nowrap;
  }
  .contacts li { list-style: none; display: flex; justify-content: flex-end; align-items: center; gap: 9px; }
  .contacts svg { width: 14px; height: 14px; flex: none; }
  .divider { width: 1px; height: 96px; background: var(--ink-light); opacity: 0.7; flex: none; }
  .person { padding-left: 16px; white-space: nowrap; }
  .person__name { font-size: 19px; font-weight: 400; }
  .person__title { font-size: 14px; margin: 2px 0 12px 6px; }
  .person__address { font-size: 12px; font-weight: 600; line-height: 18px; margin-left: 6px; }
</style>
</head>
<body>

<section class="card card--back" aria-label="Card back">
  <div class="brand"><span class="brand__square"></span>Varrow Associates</div>
  <div class="website">www.varrowpartners-example.com</div>
</section>

<section class="card card--front" aria-label="Card front">
  <div class="brand"><span class="brand__square"></span>Varrow Associates</div>
  <div class="rules"><span></span><span></span><span></span></div>
  <div class="band">
    <ul class="contacts">
      <li>347.682.1530
        <svg viewBox="0 0 16 16" aria-hidden="true"><path fill="currentColor" d="M4 2l2.5 3-1.5 1.5a8 8 0 0 0 4.5 4.5L11 9.5l3 2.5-1.5 2.5C7 14 2 9 1.5 3.5z"/></svg>
      </li>
      <li>Mvarrow@varrowpartners-example.com
        <svg viewBox="0 0 16 16" aria-hidden="true"><rect x="1" y="3" width="14" height="10" fill="currentColor"/><path d="M1 3l7 6 7-6" stroke="#0e3f6f" stroke-width="1.4" fill="none"/></svg>
      </li>
      <li>Marc.varrow
        <svg viewBox="0 0 16 16" aria-hidden="true"><circle cx="8" cy="8" r="7" fill="currentColor"/></svg>
      </li>
    </ul>
    <div class="divider"></div>
    <div class="person">
      <h1 class="person__name">Marcus Varrow</h1>
      <p class="person__title">President</p>
      <p class="person__address">2187 Tollbrook Lane,<br>Suite C, Larkfield, N.Y. 11492, USA</p>
    </div>
  </div>
</section>

</body>
</html>
```